Wine business webpage
Italian fine wines
Project: Wine business webpage
Wine business webpage -
Creative Brief
Fine and Rare Italian wine merchant
Cantina del Sole specializes in the Italy's fine and rare wines. We have special relationships with many of the greatest estates and their distributors, and are able to pass on the benefits of those relationships to our customers. We would welcome the opportunity to put our passion and knowledge to work for you!
Dislike: homepage with loads of bottles of wine, e.g. http://www.vintageharborcellars.example/
Nature
natural wood
green - Terre Verte
earth tone
top
http://www.marlowecask.example/
http://www.grapeledgerhub.example/
http://www.vinoquay.example/

```html
<!DOCTYPE html>
<html lang="en">
<head>
<meta charset="utf-8">
<title>Cantina del Sole — Fine Italian Wines</title>
<link rel="stylesheet" href="https://fonts.googleapis.com/css2?family=PT+Sans:ital,wght@0,400;0,700;1,400&family=Libre+Baskerville:wght@700&family=Great+Vibes&display=swap">
<style>
  :root {
    --damask-deep: #5e130c;
    --damask-mid: #86261a;
    --sidebar: #4a170f;
    --sidebar-dark: #36100a;
    --nav-bg: #2b0905;
    --nav-active: #d23a2a;
    --wine-red: #b3261e;
    --ink: #3a2a22;
    --muted: #6b5b52;
    --paper: #ffffff;
    --parchment: #efe3c6;
    --parchment-edge: #c6ab78;
    --table-cell: #f6ead4;
    --table-line: #d9c39b;
    --footer: #5a150f;
    --cream: #f4e6c8;
  }
  * { box-sizing: border-box; margin: 0; padding: 0; }
  html, body { width: 1200px; height: 782px; overflow: hidden; }
  body {
    font-family: "PT Sans", Arial, sans-serif;
    color: var(--ink);
    background: radial-gradient(ellipse at 50% 40%, var(--damask-mid) 0%, var(--damask-deep) 75%);
    position: relative;
  }
  .site { position: absolute; left: 233px; top: 0; width: 744px; height: 782px; background: var(--sidebar); }
  .site > * { position: absolute; }

  .brand {
    left: 0; top: 0; width: 271px; height: 192px;
    background: linear-gradient(160deg, #6d1d12 0%, var(--sidebar-dark) 100%);
    display: flex; align-items: center; justify-content: center;
  }
  .brand-name { font-family: "PT Sans", sans-serif; font-weight: 700; font-size: 26px; color: var(--cream); letter-spacing: 1px; }

  .header-photo { left: 271px; top: 0; width: 473px; height: 216px;
    background: radial-gradient(circle at 70% 40%, #e6b77a 0%, #8a4a24 40%, #3a140a 100%); }

  .main-nav { left: 271px; top: 216px; width: 473px; height: 24px; background: var(--nav-bg);
    display: flex; justify-content: space-around; align-items: center; }
  .main-nav a { color: #fff; font-size: 11px; font-weight: 700; text-decoration: none; }
  .main-nav a.active { color: var(--nav-active); }

  .content { left: 271px; top: 240px; width: 465px; height: 446px; background: var(--paper); }

  .cart { left: 19px; top: 192px; width: 242px; height: 55px; background: var(--paper);
    padding: 10px 10px 0 40px; font-size: 9px; color: var(--muted); }
  .cart-icon { position: absolute; left: 10px; top: 14px; width: 20px; height: 20px; background: #f0b92a; border-radius: 3px; }
  .cart-title { font-size: 11px; text-decoration: underline; color: #555; }
  .cart-links { position: absolute; right: 8px; top: 24px; }
  .cart-links a { color: var(--muted); }

  .categories { left: 19px; top: 259px; width: 242px; height: 288px; background: var(--parchment);
    border: 3px double var(--parchment-edge); padding: 22px 0 0 26px; }
  .categories h2 { font-family: "Libre Baskerville", Georgia, serif; font-size: 16px; color: #2a1a12; margin-bottom: 10px; }
  .categories li { list-style: none; font-size: 10.5px; font-weight: 700; color: #2a1a12; height: 23.5px; line-height: 23.5px; }
  .categories li::before { content: ""; display: inline-block; width: 0; height: 0;
    border-left: 5px solid var(--wine-red); border-top: 3.5px solid transparent; border-bottom: 3.5px solid transparent; margin-right: 8px; }

  .promo-inventory { left: 19px; top: 566px; width: 242px; height: 111px;
    background: linear-gradient(135deg, #f4e8e6 0%, #e2c1bc 60%, #b97670 100%); padding: 8px 10px; }
  .promo-inventory .script { font-family: "Great Vibes", cursive; font-size: 24px; color: var(--wine-red); text-align: right; }
  .promo-inventory .doc { font-size: 9px; font-weight: 700; color: var(--ink); margin: 6px 0 0 54px; display: flex; align-items: center; gap: 5px; }
  .promo-inventory .doc i { width: 12px; height: 12px; background: #3c7bbf; display: inline-block; }

  .welcome-photo { left: 285px; top: 252px; width: 111px; height: 108px;
    background: linear-gradient(150deg, #d9c9a8 0%, #7a2a1e 55%, #2c0d08 100%); }
  .welcome { left: 410px; top: 252px; width: 322px; }
  .welcome h1 { font-size: 13px; font-weight: 700; color: var(--wine-red); margin-bottom: 3px; }
  .welcome p { font-size: 9.5px; line-height: 11.4px; color: var(--ink); }
  .welcome .more { display: block; text-align: right; font-size: 9px; color: var(--wine-red); font-weight: 700; margin-top: 2px; }

  .rule { left: 285px; height: 1px; width: 442px; background: #e2d6c4; }

  .collection-title { left: 290px; top: 399px; font-size: 12.5px; font-weight: 700; color: var(--wine-red); }
  .collection { left: 290px; top: 420px; width: 437px; height: 137px; border-collapse: collapse; background: var(--table-cell); }
  .collection td { border: 1px dotted var(--table-line); font-size: 9.5px; color: var(--muted); padding-left: 22px; position: relative; height: 34px; width: 33.3%; }
  .collection td::before { content: ""; position: absolute; left: 10px; top: 13px;
    border-left: 5px solid var(--wine-red); border-top: 3.5px solid transparent; border-bottom: 3.5px solid transparent; }

  .promo { top: 569px; width: 214px; height: 108px; display: flex; align-items: flex-end; justify-content: center; padding-bottom: 8px; }
  .promo span { font-family: "Great Vibes", cursive; font-size: 27px; color: #fff; }
  .promo-new { left: 285px; background: linear-gradient(160deg, #e9d8a6 0%, #8d5a2a 45%, #2a1208 100%); }
  .promo-pick { left: 513px; background: linear-gradient(200deg, #f0c2c8 0%, #b45560 45%, #3b0f14 100%); }

  .site-footer { left: 0; top: 686px; width: 744px; height: 96px; background: linear-gradient(180deg, #6a1a12 0%, var(--footer) 100%); color: #fff; }
  .newsletter { position: absolute; left: 19px; top: 16px; }
  .newsletter h3 { font-size: 11px; font-weight: 700; margin-bottom: 5px; }
  .newsletter form { display: flex; gap: 3px; }
  .newsletter input { width: 160px; height: 16px; border: 0; font-size: 8px; padding: 0 4px; font-family: inherit; }
  .newsletter button { height: 16px; border: 0; background: #8b1b12; color: #fff; font-size: 8px; padding: 0 6px; font-family: inherit; }
  .follow { display: flex; align-items: center; gap: 4px; font-size: 10px; margin-top: 14px; }
  .follow i { width: 14px; height: 14px; background: #3d6fb0; display: inline-block; border-radius: 2px; }
  .footer-info { position: absolute; left: 278px; top: 18px; font-size: 9.5px; }
  .footer-links { display: flex; gap: 8px; }
  .footer-links a { color: #fff; text-decoration: none; }
  .footer-links span { color: #d9a79a; }
  .copyright { margin-top: 8px; color: #f0d8cc; }
  .cards { display: flex; gap: 4px; margin-top: 10px; }
  .cards i { width: 26px; height: 16px; background: #e9e4dc; border-radius: 2px; display: inline-block; }
</style>
</head>
<body>
<div class="site">
  <div class="brand"><span class="brand-name">Cantina del Sole</span></div>
  <div class="header-photo" role="img" aria-label="Glasses of red wine on a candlelit table"></div>
  <nav class="main-nav">
    <a class="active" href="#">Home</a><a href="#">About Us</a><a href="#">Our wines</a><a href="#">Ordering</a><a href="#">News</a><a href="#">Contact Us</a>
  </nav>
  <div class="content"></div>

  <div class="cart">
    <span class="cart-icon"></span>
    <div class="cart-title">Shopping Cart</div>
    <div>Now in your cart <b>0 items</b></div>
    <div class="cart-links"><a href="#">Login</a> | <a href="#">Register</a></div>
  </div>

  <aside class="categories">
    <h2>Categories</h2>
    <ul>
      <li>Red wine</li><li>White wine</li><li>Rose wine</li><li>Champagne</li><li>Sparkling wine</li>
      <li>Special offers</li><li>Mixed cases</li><li>Organic wines</li><li>Port</li><li>Lorem ipsum</li>
    </ul>
  </aside>

  <div class="promo-inventory" role="img" aria-label="Download inventory banner with wine glasses">
    <div class="script">Download Inventory</div>
    <div class="doc"><i></i>Lorem Ipsum Dummy</div>
    <div class="doc"><i></i>Lorem Ipsum Dummy</div>
  </div>

  <div class="welcome-photo" role="img" aria-label="Bottles of red wine resting on their side"></div>
  <section class="welcome">
    <h1>WELCOME</h1>
    <p>Lorem ipsum dolor sit amet, consectetur adipiscing elit, sed do eiusmod tempor incididunt ut labore et dolore magna aliqua. Ut enim ad minim veniam, quis nostrud exercitation ullamco laboris nisi ut aliquip ex ea commodo consequat. Lorem ipsum dolor sit amet, consectetur adipiscing elit, sed do eiusmod tempor incididunt ut labore et dolore.</p>
    <a class="more" href="#">Read More...</a>
  </section>
  <div class="rule" style="top:380px"></div>

  <h2 class="collection-title">EXCLUSIVE WINE COLLECTION</h2>
  <table class="collection">
    <tr><td>Lorem ipsum</td><td>Lorem ipsum</td><td>Lorem ipsum</td></tr>
    <tr><td>Dummy text</td><td>Dummy text</td><td>Dummy text</td></tr>
    <tr><td>sample Lorem</td><td>sample Lorem</td><td>sample Lorem</td></tr>
    <tr><td>wine txt Lorem</td><td>wine txt Lorem</td><td>wine txt Lorem</td></tr>
  </table>

  <a class="promo promo-new" href="#" role="img" aria-label="New arrivals banner with glasses of sparkling wine"><span>New Arrivals</span></a>
  <a class="promo promo-pick" href="#" role="img" aria-label="Pick of the month banner with a glass of red wine"><span>Pick of the Month</span></a>

  <footer class="site-footer">
    <div class="newsletter">
      <h3>Newsletter</h3>
      <form><input type="text" placeholder="Enter email here"><button type="button">Submit</button></form>
      <div class="follow">follow us @ <i></i><i></i><i></i></div>
    </div>
    <div class="footer-info">
      <div class="footer-links"><a href="#">Home</a><span>|</span><a href="#">About Us</a><span>|</span><a href="#">Our wines</a><span>|</span><a href="#">Ordering</a><span>|</span><a href="#">News</a><span>|</span><a href="#">Contact Us</a></div>
      <div class="copyright">Copyright © 2011 Cantina del Sole. All rights reserved.</div>
      <div class="cards"><i></i><i></i><i></i><i></i><i></i><i></i><i></i><i></i></div>
    </div>
  </footer>
</div>
</body>
</html>
```